Small environmental consultancy needs a simple but professional web design

We are a boutique environmental consultancyand contracting business located in Margaret River in the South West of Western Australia.

We have two arms
1) Consulting which offers environmental planning, management and assessment services primarily to local government and the development industry.
2) Contracting which implements on site plans and on ground works primarily involving revegetation, bush regeneration and environmental weed control.

We need a simple yet professional web design within the wordpress platform that commmunicates professionalism, experience and technical expertise without appearing too corporate.

Something like this structure appeals:
http://verdantmesh.net.au/environment-services/
or
http://www.kestrelfieldgroup.com.au/index.php

(without the image gallery function)

Target Market(s)

Local Government Officers deciding on tenders;
Developers, Engineers, Town Planning consultants looking for environmental expertise

Industry/Entity Type

Business

Number of Pages Required

5+ page

Font styles to use
Sans Serif

Colors
33a6d7
9bcb3c

Requirements
Must have
• Pages required include:
• Home
• Environmental Planning and Management
• Revegetation and Regeneration Implementation (This page can mirror the Environmental Planning and Management page exactly in structure but with different text and images)
• About Us (I think that this page can be relatively simple and generic)
• Contact (I think that this page can be very simple and generic)
Nice to have
• An ability to start out basic and quicikly establish a website presence and then build in additional drop downs and pages over time.
Should not have
• It does not need a photo gallery page;
• It does not need a major amount of space dedicated to social media and blogs etc as this is not currently particularly active area for us

```html
<!DOCTYPE html>
<html lang="en">
<head>
<meta charset="utf-8">
<title>Wandoo Vale Consulting – Environmental Planning and Management</title>
<link rel="stylesheet" href="https://fonts.googleapis.com/css2?family=PT+Sans:wght@400;700&display=swap">
<style>
  :root {
    --backdrop: #d4d5d7;
    --page: #ffffff;
    --leaf: #b3d234;
    --bark: #7a5022;
    --brand: #6b4a22;
    --heading: #2b2f33;
    --body-text: #8c8c8c;
    --nav-text: #555555;
    --footer-text: #f4ece0;
  }
  * { margin: 0; padding: 0; box-sizing: border-box; }
  html, body { width: 1200px; height: 1000px; overflow: hidden; }
  body {
    background: var(--backdrop);
    font-family: "PT Sans", Arial, sans-serif;
    position: relative;
  }
  .page {
    position: absolute; left: 113px; top: 80px;
    width: 975px; height: 840px;
    background: var(--page);
    box-shadow: 0 2px 10px rgba(0,0,0,0.12);
  }
  .brand {
    position: absolute; left: 140px; top: 16px;
    display: flex; align-items: center; gap: 10px;
  }
  .brand-mark { width: 18px; height: 18px; background: var(--leaf); }
  .brand-name {
    font-size: 24px; font-weight: 400; color: var(--brand);
    letter-spacing: 0.1px;
  }
  .main-nav { position: absolute; top: 36px; left: 0; }
  .main-nav a {
    position: absolute; white-space: nowrap;
    font-size: 6.5px; color: var(--nav-text); text-decoration: none;
  }
  .main-nav a.is-current { color: var(--brand); }
  .page-title {
    position: absolute; left: 196px; top: 96px;
    padding-left: 8px;
    border-left: 4px solid var(--leaf);
    font-size: 18px; font-weight: 700; color: var(--heading);
    line-height: 18px; text-transform: uppercase;
  }
  .copy {
    position: absolute;
    font-size: 8px; line-height: 13.4px; color: var(--body-text);
  }
  .copy p + p { margin-top: 13.4px; }
  .copy-intro { left: 196px; top: 143px; width: 282px; }
  .copy-detail { left: 495px; top: 339px; width: 288px; }
  .photo { position: absolute; }
  .photo::before {
    content: ""; position: absolute; left: 0; top: 0;
    width: 30px; height: 30px; background: var(--leaf);
  }
  .photo-seedling {
    left: 495px; top: 140px; width: 287px; height: 172px;
    background: radial-gradient(ellipse at 50% 60%, #6f6f6f 0%, #3a3a3a 35%, #0b0b0b 70%);
  }
  .photo-leaf {
    left: 196px; top: 343px; width: 285px; height: 194px;
    background: linear-gradient(150deg, #5b8a25 0%, #86b33d 40%, #4a7a1f 75%, #37601a 100%);
  }
  .photo-tree {
    left: 196px; top: 568px; width: 285px; height: 193px;
    background: linear-gradient(180deg, #dfe9ee 0%, #c9de6a 30%, #8fb12e 60%, #6c8f36 85%, #7fa24a 100%);
  }
  .site-footer {
    position: absolute; left: 0; bottom: 0;
    width: 975px; height: 49px; background: var(--bark);
  }
  .copyright {
    position: absolute; left: 196px; top: 21px;
    font-size: 7px; color: var(--footer-text);
  }
  .social { position: absolute; left: 700px; top: 21px; display: flex; gap: 10px; }
  .social span { width: 7px; height: 7px; border-radius: 50%; background: var(--footer-text); }
</style>
</head>
<body>
  <div class="page">
    <header>
      <div class="brand">
        <span class="brand-mark"></span>
        <span class="brand-name">Wandoo Vale Consulting</span>
      </div>
      <nav class="main-nav">
        <a href="#" style="left:437px">Home</a>
        <a href="#" class="is-current" style="left:480px">Environmental Planning and Management</a>
        <a href="#" style="left:618px">Revegetation and Regeneration Implementation</a>
        <a href="#" style="left:772px">About Us</a>
        <a href="#" style="left:822px">Contact</a>
      </nav>
    </header>

    <main>
      <h1 class="page-title">Environmental Planning and Management</h1>

      <div class="copy copy-intro">
        <p>Lorem ipsum dolor sit amet, doctus insolens te nam, dolor fabulas apeirian pro ex. Vis debet vulputate te, ne dicat debitis constituto qui, aperiri tibique posidonium has ne. Meis vocent te vim, ea voluptua disputando vel. Euripidis vituperata no eum, eu paulo nemore ius. Hinc fastidii ad ius, deserunt forensibus moderatius ad vis.</p>
        <p>Dico commodo facilisis ius ea, no ludus platonem ius. Nemore nostrud pri ad. Cum natum summo et. Altera lobortis mel ex, eum no erant mandamus iudicabit.</p>
        <p>Exerci soluta omittam vel at. Ullum feugiat vivendo ei per. Eam duis mutat dicta te. Id quo esse accumsan, partiendo conclusionemque per cu. Mei id autem placerat. Vel et elit mazim singulis, hinc dicant referrentur cu quo.</p>
      </div>

      <div class="photo photo-seedling" role="img" aria-label="Photo of cupped hands holding soil with a young green seedling"></div>
      <div class="photo photo-leaf" role="img" aria-label="Close-up photo of green leaf veins"></div>
      <div class="photo photo-tree" role="img" aria-label="Photo of a bright green tree standing on a grassy park lawn"></div>

      <div class="copy copy-detail">
        <p>Eam in malis feugiat adversarium, doming noster hendrerit et has. Possit recusabo referrentur mei an, nemore corrumpit id his, id mollis tetero civibus mea. His ex quidam fabellas iudicabit, ut placerat singulis salutandi est, nibh officiis scripserit quo at. Cu graeco intellegat pri, ei sed ubique postulant, ut usu persius debitis habemus. Per ut error mnesarchum, an suas viderer iudicabit mea, at viderer scriptorem ius.</p>
        <p>Pri esse sanctus id, erat inani platonem cum ex, amet reque integre an his. Ad vide discere sea, has cu percipit facilisis, id est saepe nonumy. Pri nominavi ullamcorper cu. Ea mei clita ornatus, exerci feugait consequat duo ut, at cum esse movet consul. No eam alia dolorum, at adhuc dissentias nec, ea mea idque vivendo. Simul possit sadipscing eu vel, vim alii numquam senserit ad. Mea at reque porro philosophia, apeirian ullamcorper an mea, ea quaeque persecuti vix.</p>
        <p>Ex mea modus homero, etiam congue his ea, ex hinc commune ius. Est id illud postea. Pri ea apeirian accusamus, iriure consequuntur an mel, mei maluisset patrioque an. Eu pro tantas labitur persequeris. Agam omnesque qui ei, has ei iisque debitis persequeris, justo placerat accusamus duo ex.</p>
        <p>Qui graece rationibus cu. Quo eu possim erroribus. Sed an legendos disputando, eum te apeirian recusabo. Ad nobis congue tractatos per, sea simul aliquam delenit eu. Inciderint contentiones in nam, vix ut propriae constituam appellantur.</p>
        <p>Ex mea modus homero, etiam congue his ea, ex hinc commune ius. Est id illud postea. Pri ea apeirian accusamus, iriure consequuntur an mel, mei maluisset patrioque an. Eu pro tantas labitur persequeris. Agam omnesque qui ei, has ei iisque debitis persequeris, justo placerat accusamus duo ex.</p>
      </div>
    </main>

    <footer class="site-footer">
      <p class="copyright">© Copyright 2014 by Wandoo Vale Consulting. All Rights Reserved.</p>
      <div class="social" aria-label="Social links">
        <span></span><span></span><span></span><span></span><span></span>
      </div>
    </footer>
  </div>
</body>
</html>
```